Corlith Australia Pty Ltd

I require professional business cards with our company logo. We would like something that looks sharp and unique. I have attached the logo for our business, which is an industrial electrical contracting company. But this does not need to be shown on the cards.

Requirements
Must have
• The design must be double sided and needs to have one side with our logo only and the other side with our details.
Should not have
• We do not want any lightening bolts on the designs as this is very common.

```html
<!DOCTYPE html>
<html lang="en">
<head>
<meta charset="utf-8">
<title>Corlith Australia Pty Ltd – Business Card</title>
<link rel="stylesheet" href="https://fonts.googleapis.com/css2?family=Cinzel:wght@400;600&display=swap">
<style>
  :root {
    --stage: #d9d7d2;
    --card-dark: #141414;
    --card-dark-edge: #2a2a28;
    --card-light: #ffffff;
    --gold: #c69a3e;
    --ink: #2b2b2b;
    --rule: #8a8a8a;
  }
  * { box-sizing: border-box; margin: 0; padding: 0; }
  html, body { width: 1200px; height: 871px; overflow: hidden; }
  body {
    background: var(--stage);
    font-family: "Cinzel", serif;
    display: flex;
    align-items: center;
    justify-content: center;
    gap: 40px;
  }
  .card {
    width: 540px;
    height: 309px;
    position: relative;
    box-shadow: 0 10px 24px rgba(0,0,0,.22);
  }
  /* Front */
  .card-front {
    background: radial-gradient(circle at 50% 55%, var(--card-dark-edge) 0%, var(--card-dark) 65%);
    display: flex;
    align-items: center;
    justify-content: center;
    gap: 18px;
  }
  .brand-dot {
    width: 62px; height: 62px;
    border-radius: 50%;
    background: var(--gold);
  }
  .brand-name {
    color: var(--gold);
    font-weight: 600;
    line-height: 1;
  }
  .brand-name .main { display: block; font-size: 48px; letter-spacing: 3px; }
  .brand-name .sub { display: block; font-size: 14.5px; letter-spacing: 5.2px; margin-top: 6px; }
  /* Back */
  .card-back {
    background: var(--card-light);
    color: var(--ink);
    padding: 44px 46px 0;
  }
  .person { text-align: center; }
  .person-name { font-size: 17px; font-weight: 600; letter-spacing: 1px; }
  .person-role { font-size: 12px; color: var(--gold); letter-spacing: 1px; margin-top: 2px; }
  .rule { height: 1px; background: var(--rule); }
  .rule-top { margin: 20px 0 0 8px; }
  .address { font-size: 13px; text-align: center; margin: 10px 0 8px; letter-spacing: .4px; }
  .contact-row {
    display: flex; justify-content: space-between; align-items: center;
    font-size: 12.5px; letter-spacing: .4px;
  }
  .contact-row + .contact-row { margin-top: 8px; }
  .item { display: flex; align-items: center; gap: 8px; }
  .icon { width: 11px; height: 11px; fill: var(--gold); flex: none; }
  .rule-bottom { margin-top: 10px; }
  .web .accent { color: var(--gold); }
</style>
</head>
<body>
  <section class="card card-front" aria-label="Card front">
    <span class="brand-dot"></span>
    <span class="brand-name"><span class="main">CORLITH</span><span class="sub">AUSTRALIA PTY LTD</span></span>
  </section>

  <section class="card card-back" aria-label="Card back">
    <div class="person">
      <p class="person-name">Ellis Harrow</p>
      <p class="person-role">Director</p>
    </div>
    <div class="rule rule-top"></div>
    <p class="address">PO Box 318 Kelvale NSW 2590</p>
    <div class="contact-row">
      <span class="item">
        <svg class="icon" viewBox="0 0 12 12"><path d="M3 1l2 2.5-1.2 1.3c.7 1.4 1.8 2.5 3.2 3.2L8.3 6.8 11 8.7 10 11C5.5 10.7 1.3 6.5 1 2z"/></svg>
        02 4710 5382
      </span>
      <span class="item">
        <svg class="icon" viewBox="0 0 12 12"><path d="M3 1l2 2.5-1.2 1.3c.7 1.4 1.8 2.5 3.2 3.2L8.3 6.8 11 8.7 10 11C5.5 10.7 1.3 6.5 1 2z"/></svg>
        0412 907 245
      </span>
    </div>
    <div class="contact-row">
      <span class="item">
        <svg class="icon" viewBox="0 0 12 12"><path d="M0 2h12v8H0z M1 3l5 3.5L11 3" fill="none" stroke="var(--gold)" stroke-width="1.2"/></svg>
        ellis@corlithaustralia.com.au
      </span>
      <span class="item web">
        <svg class="icon" viewBox="0 0 12 12"><circle cx="6" cy="6" r="5" fill="none" stroke="var(--gold)" stroke-width="1.2"/><path d="M1 6h10M6 1c-2.5 3-2.5 7 0 10M6 1c2.5 3 2.5 7 0 10" fill="none" stroke="var(--gold)" stroke-width="1"/></svg>
        www.<span class="accent">corlith</span>.com
      </span>
    </div>
    <div class="rule rule-bottom"></div>
  </section>
</body>
</html>
```